modern, IT themed business card for IT accelerator

Design a business card for tech oriented business accelerator. Prevailing color shall be orange.
we are operating in emerging markets and our mission is to provide co-working space, mentorship/coaching and ultimately seed financing IT startups.
also, we are helping financed ITs in obtaining next round financing, and to this end we are meeting with non IT/finance people and investment professionals..
that means card shall be designed to "impress" not only IT people (mostly liberal) but finance (more conservative)

Industry/Entity Type

Investment

Contact Information for Business Card

Company Name: Pelor Founders Yard
Name: Temur Kobaladze
Position: Partner
Address: 14, N Abashidze St., Tbilisi 0162, Georgia
Tel: +995599438165
Email: t.kobaladze@pelorhub.ge
Website: www.pelorhub.ge

Font styles to use
Sans Serif

Requirements
Must have
• Attached are logos of the company (portrait & landscape) choose any
Nice to have
• industry is IT and finance (in fact, financing IT startups). therefore design might have IT theme (inspiration from web or software designs)

```html
<!DOCTYPE html>
<html lang="en">
<head>
<meta charset="utf-8">
<title>Pelor Founders Yard – Business Card</title>
<link href="https://fonts.googleapis.com/css2?family=Barlow:wght@400;500&display=swap" rel="stylesheet">
<style>
  :root {
    --page-bg: #f4f4f4;
    --orange: #f08c1f;
    --orange-deep: #e06f17;
    --orange-light: #f7a33a;
    --silver-light: #ffffff;
    --silver-mid: #ececec;
    --silver-dark: #d4d4d6;
    --logo-grey: #6d6e72;
    --text-grey: #5e5f63;
    --white: #ffffff;
  }
  * { margin: 0; padding: 0; box-sizing: border-box; }
  html, body {
    width: 1200px;
    height: 900px;
    overflow: hidden;
    background: var(--page-bg);
    font-family: "Barlow", Arial, sans-serif;
  }
  .canvas {
    position: relative;
    width: 1200px;
    height: 900px;
    display: flex;
    align-items: center;
    justify-content: center;
    gap: 50px;
  }
  .card {
    position: relative;
    width: 520px;
    height: 310px;
    border-radius: 24px;
    overflow: hidden;
    box-shadow: 0 14px 30px rgba(0,0,0,0.14);
  }
  .card-texture {
    position: absolute;
    inset: 0;
  }
  /* Front */
  .card--front {
    background: linear-gradient(135deg, var(--orange-light) 0%, var(--orange) 45%, var(--orange-deep) 100%);
  }
  .card--front .card-texture {
    background: radial-gradient(circle at 58% 50%, rgba(255,255,255,0.16) 0%, rgba(255,255,255,0.04) 45%, rgba(255,255,255,0) 70%);
  }
  .brand {
    position: absolute;
    display: flex;
    align-items: center;
    gap: 16px;
  }
  .card--front .brand {
    left: 80px;
    top: 118px;
  }
  .brand-dot {
    width: 58px;
    height: 58px;
    border-radius: 50%;
    flex: none;
  }
  .card--front .brand-dot { background: var(--white); }
  .brand-name {
    font-weight: 500;
    font-size: 32px;
    line-height: 1.05;
    letter-spacing: 0.5px;
  }
  .card--front .brand-name { color: var(--white); }

  /* Back */
  .card--back {
    background: linear-gradient(120deg, var(--silver-mid) 0%, var(--silver-light) 40%, var(--silver-mid) 70%, var(--silver-dark) 100%);
  }
  .card--back .card-texture {
    background: radial-gradient(circle at 72% 40%, rgba(255,255,255,0.7) 0%, rgba(255,255,255,0) 60%);
  }
  .holder {
    position: absolute;
    right: 30px;
    top: 30px;
    text-align: right;
  }
  .holder-name {
    color: var(--orange);
    font-size: 21px;
    font-weight: 400;
  }
  .holder-role {
    color: var(--text-grey);
    font-size: 11px;
    margin-top: 1px;
  }
  .card--back .brand {
    left: 34px;
    top: 84px;
  }
  .card--back .brand-dot { background: var(--orange); }
  .card--back .brand-name { color: var(--logo-grey); font-size: 30px; }
  .contacts {
    position: absolute;
    left: 28px;
    bottom: 26px;
    list-style: none;
    color: var(--text-grey);
    font-size: 14px;
    line-height: 19px;
  }
  .contacts li {
    display: flex;
    align-items: flex-start;
    gap: 6px;
  }
  .contact-icon {
    width: 14px;
    height: 14px;
    margin-top: 2px;
    flex: none;
    fill: var(--orange);
  }
</style>
</head>
<body>
<main class="canvas">

  <section class="card card--front" aria-label="Card front">
    <div class="card-texture" role="img" aria-label="Faint technology ring and polygon pattern on orange"></div>
    <div class="brand">
      <span class="brand-dot"></span>
      <span class="brand-name">Pelor<br>Founders Yard</span>
    </div>
  </section>

  <section class="card card--back" aria-label="Card back">
    <div class="card-texture" role="img" aria-label="Faint technology ring and polygon pattern on silver"></div>
    <div class="holder">
      <p class="holder-name">Temur Kobaladze</p>
      <p class="holder-role">Partner</p>
    </div>
    <div class="brand">
      <span class="brand-dot"></span>
      <span class="brand-name">Pelor<br>Founders Yard</span>
    </div>
    <ul class="contacts">
      <li>
        <svg class="contact-icon" viewBox="0 0 24 24" aria-hidden="true"><path d="M6.6 10.8a15.1 15.1 0 0 0 6.6 6.6l2.2-2.2c.3-.3.7-.4 1-.2 1.1.4 2.3.6 3.6.6.6 0 1 .4 1 1V20c0 .6-.4 1-1 1A17 17 0 0 1 3 4c0-.6.4-1 1-1h3.5c.6 0 1 .4 1 1 0 1.3.2 2.5.6 3.6.1.3 0 .7-.2 1z"/></svg>
        <span>+995599438165</span>
      </li>
      <li>
        <svg class="contact-icon" viewBox="0 0 24 24" aria-hidden="true"><path d="M3 5h18c.6 0 1 .4 1 1v12c0 .6-.4 1-1 1H3c-.6 0-1-.4-1-1V6c0-.6.4-1 1-1zm1 2.3V17h16V7.3l-8 5.4z M5 7l7 4.7L19 7z"/></svg>
        <span>t.kobaladze@pelorhub.ge</span>
      </li>
      <li>
        <svg class="contact-icon" viewBox="0 0 24 24" aria-hidden="true"><path d="M12 2a10 10 0 1 0 0 20 10 10 0 0 0 0-20zm6.9 6h-2.9a15 15 0 0 0-1.4-3.6A8 8 0 0 1 18.9 8zM12 4c.8 1.2 1.5 2.5 1.9 4h-3.8c.4-1.5 1.1-2.8 1.9-4zM4.3 14a8 8 0 0 1 0-4h3.4a16 16 0 0 0 0 4zm.8 2h2.9c.3 1.3.8 2.5 1.4 3.6A8 8 0 0 1 5.1 16zM8 8H5.1a8 8 0 0 1 4.3-3.6C8.8 5.5 8.3 6.7 8 8zm4 12c-.8-1.2-1.5-2.5-1.9-4h3.8c-.4 1.5-1.1 2.8-1.9 4zm2.3-6H9.7a14 14 0 0 1 0-4h4.6a14 14 0 0 1 0 4zm.3 5.6c.6-1.1 1.1-2.3 1.4-3.6h2.9a8 8 0 0 1-4.3 3.6zm1.7-5.6a16 16 0 0 0 0-4h3.4a8 8 0 0 1 0 4z"/></svg>
        <span>www.pelorhub.ge</span>
      </li>
      <li>
        <svg class="contact-icon" viewBox="0 0 24 24" aria-hidden="true"><path d="M12 3 2 12h3v9h6v-6h2v6h6v-9h3z"/></svg>
        <span>14, N Abashidze St.,<br>Tbilisi 0162, Georgia</span>
      </li>
    </ul>
  </section>

</main>
</body>
</html>
```